Creative Fitness Studio Feature Wall

Two feature walls within functional fitness studio, they need to be on brand and have a WOW factor.
Designed to inspire and motivate people to live a fit and healthy lifestyle whilst working out and bringing life to the studio, as an uplifting and inviting environment.

Please see current walls and also visit website www.velta4.com.au for inspiration.
Updates

Target Market(s)

health and fitness, healthy lifestyle

Industry/Entity Type

Fitness

Font styles to use
Other font styles liked:
• gothic

Colors

Designer to choose colors to be used in the design.

Requirements
Must have
• inspiration from website www.velta4.com.au ........... brand consistency
Nice to have
• WOW factor......... walk into the gym and it draws your attention.
Should not have
• Overly muscly people (bodybuilders)

```html
<!DOCTYPE html>
<html lang="en">
<head>
<meta charset="utf-8">
<title>Velta4 Fitness – Feature Wall</title>
<link rel="stylesheet" href="https://fonts.googleapis.com/css2?family=Crimson+Text:wght@700&display=swap">
<style>
  :root {
    --bg: #000000;
    --brand-green: #8cc63f;
    --text-white: #ffffff;
    --photo-dark: #262626;
    --photo-mid: #3e3e3e;
    --athlete-warm: #9c7a66;
    --athlete-cool: #5d7f88;
  }
  * { margin: 0; padding: 0; box-sizing: border-box; }
  html, body {
    width: 1200px;
    height: 800px;
    overflow: hidden;
    background: var(--bg);
  }
  .wall {
    position: relative;
    width: 1200px;
    height: 800px;
    background: var(--bg);
    overflow: hidden;
    font-family: "Crimson Text", Georgia, serif;
    font-weight: 700;
  }
  .wall__shapes {
    position: absolute;
    inset: 0;
  }
  .backdrop-photo {
    position: absolute;
    left: 0;
    top: 0;
    width: 640px;
    height: 800px;
    background: radial-gradient(ellipse at 45% 40%, var(--photo-mid) 0%, var(--photo-dark) 45%, rgba(0,0,0,0) 80%);
    opacity: 0.6;
  }
  .athlete-photo {
    position: absolute;
    left: 766px;
    top: 0;
    width: 346px;
    height: 800px;
    border-radius: 24px 24px 0 0;
    background: linear-gradient(180deg, var(--athlete-warm) 0%, var(--athlete-cool) 55%, var(--athlete-warm) 100%);
  }
  .slogan__word,
  .slogan__line {
    position: absolute;
    left: 60px;
    line-height: 1;
    white-space: nowrap;
  }
  .slogan__word {
    color: var(--brand-green);
    font-size: 90px;
  }
  .slogan__line {
    color: var(--text-white);
    font-size: 41px;
  }
  .slogan__word--motivation { top: 42px; }
  .slogan__line--started    { top: 124px; }
  .slogan__word--habit      { top: 181px; }
  .slogan__line--going      { top: 262px; }
  .slogan__word--attitude   { top: 315px; }
  .slogan__line--well       { top: 398px; }
  .brand-name__main,
  .brand-name__sub {
    position: absolute;
    color: var(--text-white);
    line-height: 1;
    white-space: nowrap;
  }
  .brand-name__main {
    left: 62px;
    top: 621px;
    font-size: 96px;
    letter-spacing: 1px;
  }
  .brand-name__sub {
    left: 138px;
    top: 730px;
    font-size: 32px;
    letter-spacing: 8px;
  }
</style>
</head>
<body>
  <main class="wall">
    <div class="backdrop-photo" role="img" aria-label="Faded black-and-white photo of a smiling woman training with a dumbbell"></div>

    <svg class="wall__shapes" width="1200" height="800" viewBox="0 0 1200 800" aria-hidden="true">
      <polygon points="674,0 1200,0 1200,800 1135,800" fill="var(--brand-green)"/>
    </svg>

    <div class="athlete-photo" role="img" aria-label="Photo of a fit woman in sportswear curling a dumbbell"></div>

    <section class="slogan">
      <span class="slogan__word slogan__word--motivation">Motivation</span>
      <span class="slogan__line slogan__line--started">Is What Gets You Started</span>
      <span class="slogan__word slogan__word--habit">Habit</span>
      <span class="slogan__line slogan__line--going">Is What Keeps You Going</span>
      <span class="slogan__word slogan__word--attitude">Attitude</span>
      <span class="slogan__line slogan__line--well">Determines How Well You Do It</span>
    </section>

    <div class="brand-name">
      <span class="brand-name__main">VELTA4</span>
      <span class="brand-name__sub">FITNESS</span>
    </div>
  </main>
</body>
</html>
```